" Atua no ramo de diagnostico por imagem veterinário realizando exames de raio x, ultrassonografia, tomografia computadorizada e ressonância magnética para animais de companhia. "

```html
<!DOCTYPE html>
<html lang="pt-BR">
<head>
<meta charset="utf-8">
<title>IMAVET – Papel timbrado</title>
<link href="https://fonts.googleapis.com/css2?family=Arimo:wght@400;700&display=swap" rel="stylesheet">
<style>
  :root{
    --bg:#e4e5e7;
    --paper:#ffffff;
    --ink:#1c1c1c;
    --brand-blue:#23566f;
    --brand-green:#2f9a4a;
    --band-blue:#1f4e6b;
    --muted:#4a4f55;
  }
  html,body{margin:0;padding:0;width:1200px;height:1200px;overflow:hidden;background:var(--bg);}
  .sheet{
    position:absolute;left:185px;top:25px;width:830px;height:1150px;
    background:var(--paper);box-shadow:0 4px 18px rgba(0,0,0,.18);
    font-family:"Arimo",Arial,sans-serif;color:var(--ink);overflow:hidden;
  }
  .brand{
    position:absolute;top:95px;left:0;right:0;
    display:flex;justify-content:center;align-items:center;gap:20px;
  }
  .brand-square{width:72px;height:72px;border-radius:8px;background:var(--brand-blue);}
  .brand-text{display:flex;flex-direction:column;}
  .brand-name{font-weight:700;font-size:64px;line-height:1;color:var(--brand-blue);letter-spacing:2px;}
  .brand-tag{font-weight:400;font-size:14px;color:var(--muted);letter-spacing:1px;margin-top:6px;text-transform:uppercase;}
  .letter-body{
    position:absolute;top:285px;left:70px;right:70px;
    font-size:18.5px;line-height:1.3;
  }
  .letter-body p{margin:0 0 22px;}
  .contacts{
    position:absolute;top:955px;left:135px;right:90px;
    display:grid;grid-template-columns:1fr 1fr;row-gap:14px;column-gap:30px;
    font-size:17px;color:var(--muted);
  }
  .contact{display:flex;align-items:flex-start;gap:10px;}
  .contact svg{flex:none;margin-top:2px;}
  .contact.small{font-size:14px;}
  .bands{position:absolute;left:0;bottom:58px;width:830px;height:40px;}
</style>
</head>
<body>
<div class="sheet">
  <header class="brand">
    <div class="brand-square"></div>
    <div class="brand-text">
      <span class="brand-name">IMAVET</span>
      <span class="brand-tag">Exames de imagem para cães e gatos</span>
    </div>
  </header>

  <main class="letter-body">
    <p>Lorem ipsum dolor sit amet, ne vis ipsum detraxit forensibus. Vim ad dicta disputando, facete expetendis sea ne. At omnium vidisse referrentur cum. Id vel quas dicunt platonem, vim at veniam commodo adversarium, per an fabulas reformidans. Ad delenit appareat vel, denique minimum intellegam et has.</p>
    <p>Nec ex albucius moderatius. Essent salutandi pri id, no has porro commune. Iusto dolore definitionem mea et, eleifend salutatus at vel. Ignota apeirian duo an, nam no liber cetero, sit legere sapient quaestio te. Sit ei oratio invenire platonem, nam ex congue primis conclusionemque, eos case albucius voluptatum cu.</p>
    <p>Sea ea summo senserit, ne pri accusam electram corrumpit. Hinc forensibus cu est, sed id invenire persequeris. Accumsan lucilius reformidans et sea. Duo laudem dolorem ne.</p>
    <p>Illud minimum duo ut. Docendi abhorreant quo no, duo ad appetere eleifend persequeris, blandit assentior disputationi no mea. Pro id movet cetero aeterno, in prima nusquam deseruisse pri, errem petentium et vis. Mollis aliquip admodum nec te, eu falli nullam utroque nec, falli invenire iudicabit eu eam.</p>
    <p>Mei viderer adipisci corrumpit te, dissentias intellegebat per eu. An solum decore luptatum mei, in brute scripta disputationi vel. Semper gubergren quo no. In quo regione placerat, quod legere nam ad.</p>
  </main>

  <footer class="contacts">
    <div class="contact small">
      <svg width="16" height="16" viewBox="0 0 24 24"><path fill="#23566f" d="M6.6 10.8a15.1 15.1 0 0 0 6.6 6.6l2.2-2.2c.3-.3.7-.4 1-.2 1.1.4 2.3.6 3.6.6.6 0 1 .4 1 1V20c0 .6-.4 1-1 1A17 17 0 0 1 3 4c0-.6.4-1 1-1h3.5c.6 0 1 .4 1 1 0 1.3.2 2.5.6 3.6.1.3 0 .7-.2 1z"/></svg>
      <span>(00) 00000.0000 / 00000.0000</span>
    </div>
    <div class="contact">
      <svg width="18" height="18" viewBox="0 0 24 24"><circle cx="12" cy="12" r="9.5" fill="none" stroke="#23566f" stroke-width="2"/><path d="M2.5 12h19M12 2.5c3 3 3 16 0 19M12 2.5c-3 3-3 16 0 19" fill="none" stroke="#23566f" stroke-width="1.6"/></svg>
      <span>www.imavet.com.br</span>
    </div>
    <div class="contact">
      <svg width="18" height="18" viewBox="0 0 24 24"><circle cx="12" cy="12" r="4" fill="none" stroke="#23566f" stroke-width="2.2"/><path d="M16 8v5.5c0 1.7 2.6 1.7 3.5 0A9 9 0 1 0 16 20" fill="none" stroke="#23566f" stroke-width="2.2"/></svg>
      <span>contato@imavet.com.br</span>
    </div>
    <div class="contact small">
      <svg width="16" height="18" viewBox="0 0 24 24"><path fill="#23566f" d="M12 2a7 7 0 0 0-7 7c0 5.2 7 13 7 13s7-7.8 7-13a7 7 0 0 0-7-7zm0 9.5A2.5 2.5 0 1 1 12 6.5a2.5 2.5 0 0 1 0 5z"/></svg>
      <span>End. completo, 00, Bairro<br>CEP 0000.0000 - Cidade-SP</span>
    </div>
  </footer>

  <svg class="bands" viewBox="0 0 830 40" preserveAspectRatio="none">
    <polygon points="0,10 610,10 590,40 0,40" fill="var(--band-blue)"/>
    <polygon points="616,10 830,0 830,40 596,40" fill="var(--brand-green)"/>
  </svg>
</div>
</body>
</html>
```